One slide graphic for website

I am designing a series of sliders for my website http://new.quillhartmedia.example

The slide I am trying to create has the following message:

EVERY company is a media company.
Empower yours now!

Learn More >

The ideas I have had for imagery are an office building with the letters 'Every Company is a Media Company' either shone onto the building or letters on the building roof ledge ect.

Aby ideas you may have to improve on this would be appreciated.

The idea behind the slide is to promote a software application which gives marketing professionals the chance to increase their media coverage. The message also encourages companies to create their own news on a number of platforms as the media landscape has changed so much. Look at the blue heron stunt whereby they generated 10 million views on clipvault using PR alone.

Good luck and I look forward to seeing your ideas.

Martin

```html
<!DOCTYPE html>
<html lang="en">
<head>
<meta charset="utf-8">
<title>Quillhart – Every company is a media company</title>
<link href="https://fonts.googleapis.com/css2?family=Open+Sans:ital,wght@0,300;0,400;0,600;0,700;1,300;1,400&display=swap" rel="stylesheet">
<style>
  :root{
    --brand-green:#2a9a4f;
    --nav-green:#2a9244;
    --nav-green-dark:#1d6e33;
    --orange:#ff9900;
    --purple:#8e44ad;
    --hero-teal:#66b39e;
    --hero-deep:#2f7f68;
    --caption-band:rgba(25,45,40,0.88);
    --ink:#333333;
    --ink-soft:#555555;
    --grey-icon:#4a4a4a;
    --white:#ffffff;
  }
  *{margin:0;padding:0;box-sizing:border-box}
  html,body{width:1200px;height:849px;overflow:hidden;background:var(--white);font-family:"Open Sans",sans-serif;color:var(--ink)}
  .page{position:relative;width:1200px;height:849px;overflow:hidden}

  .site-header{position:absolute;left:0;top:0;width:1200px;height:111px}
  .brand-name{position:absolute;left:145px;top:30px;font-size:40px;font-weight:400;letter-spacing:-0.5px;color:var(--brand-green);line-height:48px}
  .contact-line{position:absolute;left:771px;top:16px;display:flex;align-items:center;gap:6px}
  .phone{font-size:18px;color:#666;font-weight:400;margin-right:8px}
  .social-dot{width:21px;height:21px;border-radius:50%;background:var(--grey-icon)}
  .header-actions{position:absolute;left:817px;top:52px;display:flex;gap:6px}
  .action-btn{display:flex;align-items:center;gap:6px;height:27px;padding:0 10px 0 6px;border-radius:6px;color:var(--white);font-size:15px;font-weight:700;font-style:italic;text-transform:uppercase}
  .action-btn svg{flex:none}
  .action-demo{background:var(--purple);width:126px}
  .action-login{background:var(--orange);width:88px}

  .main-nav{position:absolute;left:0;top:111px;width:1200px;height:47px;background:linear-gradient(var(--nav-green-dark) 0 5px,var(--nav-green) 5px)}
  .nav-list{position:absolute;left:145px;top:4px;display:flex;list-style:none;height:43px}
  .nav-list li{display:flex;align-items:center;padding:0 14px;font-size:12px;font-weight:700;color:var(--white);border-right:1px solid rgba(0,0,0,0.18);letter-spacing:0.1px}
  .nav-list li.is-current{background:var(--orange)}

  .hero{position:absolute;left:0;top:158px;width:1200px;height:415px;background:var(--hero-teal)}
  .hero-photo{position:absolute;left:142px;top:0;width:916px;height:415px;
    background:
      radial-gradient(ellipse 45% 60% at 70% 55%,rgba(30,90,70,0.75),rgba(30,90,70,0) 70%),
      radial-gradient(ellipse 35% 45% at 35% 70%,rgba(40,110,88,0.55),rgba(40,110,88,0) 75%),
      linear-gradient(90deg,rgba(102,179,158,0),rgba(60,140,115,0.5) 20%,rgba(60,140,115,0.5) 85%,rgba(102,179,158,0))}
  .hero-caption{position:absolute;left:0;top:327px;width:1200px;height:85px;background:var(--caption-band)}
  .hero-headline{position:absolute;left:145px;top:22px;font-size:26px;font-weight:400;color:var(--white);letter-spacing:-0.2px}
  .hero-cta{position:absolute;left:852px;top:18px;width:185px;height:49px;border-radius:14px 0 14px 0;background:var(--orange);color:#222;font-size:22px;font-weight:400;display:flex;align-items:center;justify-content:center}

  .tagline{position:absolute;left:0;top:586px;width:1200px;text-align:center;font-size:32px;font-weight:300;font-style:italic;color:var(--ink);line-height:35px}

  .features{position:absolute;left:147px;top:693px;display:flex;gap:11px}
  .feature{position:relative;width:217px;height:170px;text-align:center}
  .feature::before,.feature::after{content:"";position:absolute;top:24px;bottom:0;width:1px;background:linear-gradient(#ededed,#dcdcdc)}
  .feature::before{left:0}
  .feature::after{right:0}
  .feature-title{font-size:22px;font-style:italic;font-weight:400;color:var(--ink);line-height:30px}
  .feature-icon{display:block;margin:12px auto 0;height:70px}
  .feature-text{margin-top:13px;padding:0 22px;font-size:12px;font-style:italic;color:var(--ink-soft);line-height:18px}
</style>
</head>
<body>
<div class="page">

  <header class="site-header">
    <div class="brand-name">QUILLHART</div>
    <div class="contact-line">
      <span class="phone">t. +44 (0)1632 960418</span>
      <span class="social-dot"></span>
      <span class="social-dot"></span>
      <span class="social-dot"></span>
    </div>
    <div class="header-actions">
      <span class="action-btn action-demo">
        <svg width="19" height="19" viewBox="0 0 20 20"><circle cx="10" cy="10" r="9" fill="#fff"/><path d="M5 10h8M10 6l4 4-4 4" stroke="#8e44ad" stroke-width="2.4" fill="none" stroke-linecap="round" stroke-linejoin="round"/></svg>
        Free Demo
      </span>
      <span class="action-btn action-login">
        <svg width="19" height="19" viewBox="0 0 20 20"><circle cx="10" cy="10" r="9" fill="#fff"/><path d="M5 10h8M10 6l4 4-4 4" stroke="#ff9900" stroke-width="2.4" fill="none" stroke-linecap="round" stroke-linejoin="round"/></svg>
        Login
      </span>
    </div>
  </header>

  <nav class="main-nav">
    <ul class="nav-list">
      <li class="is-current">HOME</li>
      <li>SOFTWARE</li>
      <li>INDUSTRIES</li>
      <li>NEWS</li>
      <li>WEBINARS</li>
      <li>FREE DOWNLOADS</li>
      <li>OUR STORY</li>
      <li>OUR VALUES</li>
      <li>CONTACT US</li>
    </ul>
  </nav>

  <section class="hero">
    <div class="hero-photo" role="img" aria-label="Green-tinted upward view of a modern glass office building with a curved facade and a triangular glazed roof"></div>
    <div class="hero-caption">
      <p class="hero-headline">Every company is a media company. Empower Your Now!</p>
      <span class="hero-cta">LEARN MORE</span>
    </div>
  </section>

  <p class="tagline">Fast and easy way to send press releases, manage your<br>news page &amp; nurture your reputation</p>

  <section class="features">
    <svg width="0" height="0" style="position:absolute">
      <defs>
        <linearGradient id="iconGrad" x1="0" y1="0" x2="0" y2="1">
          <stop offset="0" stop-color="#26b08a"/>
          <stop offset="1" stop-color="#1e8a3e"/>
        </linearGradient>
      </defs>
    </svg>

    <div class="feature">
      <h3 class="feature-title">Cloud-based</h3>
      <svg class="feature-icon" width="100" height="70" viewBox="0 0 100 70">
        <path d="M22 62a18 18 0 0 1-2-36 26 26 0 0 1 50-6 20 20 0 0 1 10 42z" fill="url(#iconGrad)"/>
        <path d="M50 22 32 42h11v18h14V42h11z" fill="#fff"/>
      </svg>
      <p class="feature-text">Manage your marketing and PR campaigns with easy use</p>
    </div>

    <div class="feature">
      <h3 class="feature-title">Big Database</h3>
      <svg class="feature-icon" width="70" height="76" viewBox="0 0 70 76">
        <ellipse cx="35" cy="10" rx="32" ry="9" fill="url(#iconGrad)"/>
        <path d="M3 14v12c0 5 14 9 32 9s32-4 32-9V14c0 5-14 9-32 9S3 19 3 14z" fill="url(#iconGrad)"/>
        <path d="M3 31v12c0 5 14 9 32 9s32-4 32-9V31c0 5-14 9-32 9S3 36 3 31z" fill="url(#iconGrad)"/>
        <path d="M3 48v12c0 5 14 9 32 9s32-4 32-9V48c0 5-14 9-32 9S3 53 3 48z" fill="url(#iconGrad)"/>
      </svg>
      <p class="feature-text">Database of 20,000 journalists with the added ability to be able</p>
    </div>

    <div class="feature">
      <h3 class="feature-title">Secure &amp; Safe</h3>
      <svg class="feature-icon" width="78" height="74" viewBox="0 0 78 74">
        <path d="M2 4h28l6 8h40v60H2z" fill="url(#iconGrad)"/>
        <rect x="30" y="42" width="18" height="15" rx="2" fill="#fff"/>
        <path d="M33 42v-5a6 6 0 0 1 12 0v5" stroke="#fff" stroke-width="3" fill="none"/>
      </svg>
      <p class="feature-text">Daily backups and hosting on Stackhaven dedicated servers</p>
    </div>

    <div class="feature">
      <h3 class="feature-title">Save Time</h3>
      <svg class="feature-icon" width="80" height="80" viewBox="0 0 80 80">
        <path d="M40 8a32 32 0 1 1-28 16" stroke="url(#iconGrad)" stroke-width="8" fill="none"/>
        <path d="M6 8 24 6 18 26z" fill="#26b08a"/>
        <path d="M40 22v22H56" stroke="#1e8a3e" stroke-width="6" fill="none"/>
      </svg>
      <p class="feature-text">Quillhart brilliantly wins media coverage and distributes your</p>
    </div>
  </section>

</div>
</body>
</html>
```